Brindle Property Management Vendor Recruiting Email

We need a digital flyer to email and post on Social media to attract new vendors to our website to apply to complete maintenance work on our clients homes. I have one flyer we had produced recently that we are un-happy with. It is attached.

The example given is what we do not want!! We do not want any of the pictures used from the existing one

Target Market(s)

Construction companies and handyman

Industry/Entity Type

Residential maintenance and repairs

Requirements
Must have
• Join our team as the header not become a vendor

```html
<!DOCTYPE html>
<html lang="en">
<head>
<meta charset="utf-8">
<title>Brindle Property Management – Vendor Flyer</title>
<link href="https://fonts.googleapis.com/css2?family=Montserrat:wght@300;400;500;700;800;900&display=swap" rel="stylesheet">
<style>
  :root{
    --page-bg:#e6e6e8;
    --ink-dark:#16151a;
    --card-bg:#f1f1f4;
    --card-text:#1d1d22;
    --white:#ffffff;
    --accent-blue:#3cb8ea;
    --accent-purple:#8a4fd2;
    --accent-pink:#b45fc4;
  }
  *{box-sizing:border-box;margin:0;padding:0}
  html,body{width:927px;height:1200px;overflow:hidden;background:var(--page-bg)}
  body{font-family:"Montserrat",sans-serif;position:relative}
  .flyer{position:absolute;left:39px;top:0;width:848px;height:1200px;background:var(--ink-dark);overflow:hidden}
  .hero-photo{position:absolute;left:0;top:0;width:848px;height:563px;
    background:
      linear-gradient(180deg,rgba(0,0,0,0) 55%,rgba(0,0,0,.25) 100%),
      linear-gradient(165deg,#eef0f1 0%,#dcdcdb 22%,#6f6766 40%,#8f8984 58%,#b9b3aa 75%,#7c7a60 100%);}
  .hero-title{position:absolute;left:78px;top:232px;color:var(--white);text-shadow:4px 4px 0 rgba(0,0,0,.55)}
  .hero-title .lead{display:block;font-weight:400;font-size:56px;letter-spacing:-1px;line-height:1}
  .hero-title .main{display:block;font-weight:900;font-size:98px;letter-spacing:-3px;line-height:1;margin-top:8px}
  .benefit{position:absolute;top:429px;width:228px;height:237px;background:var(--card-bg);border-radius:14px;
    text-align:center;padding:0 10px}
  .benefit svg{display:block;margin:34px auto 0;width:60px;height:60px}
  .benefit p{margin-top:24px;font-size:15.5px;line-height:20px;color:var(--card-text)}
  .benefit--approval{left:64px}
  .benefit--materials{left:314px}
  .benefit--payment{left:563px}
  .requirements-title{position:absolute;left:80px;top:722px;color:var(--white);line-height:1}
  .requirements-title .light{display:block;font-weight:300;font-size:48px;letter-spacing:1px}
  .requirements-title .bold{display:block;font-weight:800;font-size:47px;margin-top:12px}
  .requirements-list{position:absolute;left:82px;top:866px;list-style:none;color:var(--white);font-size:15.5px}
  .requirements-list li{height:26px;line-height:26px;position:relative;padding-left:16px}
  .requirements-list li::before{content:"";position:absolute;left:0;top:11px;width:6px;height:6px;border-radius:50%;background:var(--accent-blue)}
  .requirements-list li:nth-child(n+3)::before{background:var(--accent-purple)}
  .requirements-list li:nth-child(n+5)::before{background:var(--accent-pink)}
  .brand{position:absolute;left:563px;top:892px;width:240px;text-align:center;color:var(--white);
    font-weight:700;font-size:23px;line-height:30px;letter-spacing:1px}
  .brand .mark{display:block;width:46px;height:46px;border-radius:50%;background:var(--accent-blue);margin:0 auto 14px}
  .contact-phone{position:absolute;left:80px;top:1072px;color:var(--white);font-weight:700;font-size:27px}
  .contact-web{position:absolute;left:80px;top:1106px;color:var(--white);font-weight:300;font-size:25px;letter-spacing:1.5px}
  .contact-web b{font-weight:800}
</style>
</head>
<body>
  <main class="flyer">
    <div class="hero-photo" role="img" aria-label="Photo of contractors reviewing plans in front of a house under construction"></div>

    <h1 class="hero-title"><span class="lead">JOIN OUR</span><span class="main">TEAM</span></h1>

    <svg width="0" height="0" style="position:absolute">
      <defs>
        <linearGradient id="iconGrad" x1="0" y1="0" x2="1" y2="1">
          <stop offset="0" stop-color="#3cb8ea"/>
          <stop offset="1" stop-color="#9a4fd0"/>
        </linearGradient>
      </defs>
    </svg>

    <section class="benefit benefit--approval">
      <svg viewBox="0 0 62 62" aria-hidden="true">
        <path d="M2 4h58v40H40l-9 12-9-12H2z" fill="url(#iconGrad)"/>
        <path d="M18 24l9 9 17-17" fill="none" stroke="#fff" stroke-width="6" stroke-linecap="round" stroke-linejoin="round"/>
      </svg>
      <p>95% approval rating<br>on all submitted<br>estimates. Guaranteed<br>work volume.</p>
    </section>

    <section class="benefit benefit--materials">
      <svg viewBox="0 0 62 62" aria-hidden="true">
        <path d="M2 8h9l7 30h30l6-22H17" fill="none" stroke="url(#iconGrad)" stroke-width="5" stroke-linejoin="round" stroke-linecap="round"/>
        <rect x="18" y="20" width="32" height="14" rx="2" fill="url(#iconGrad)"/>
        <circle cx="22" cy="50" r="5" fill="url(#iconGrad)"/>
        <circle cx="45" cy="50" r="5" fill="url(#iconGrad)"/>
        <circle cx="52" cy="12" r="9" fill="#3cb8ea"/>
        <path d="M52 7v9M48 12l4 4 4-4" fill="none" stroke="#fff" stroke-width="2.2" stroke-linecap="round"/>
      </svg>
      <p>Material purchasing<br>program to help vendors<br>with low capital or<br>no or bad credit.</p>
    </section>

    <section class="benefit benefit--payment">
      <svg viewBox="0 0 62 62" aria-hidden="true">
        <path d="M31 4l22 8v18c0 14-10 24-22 28C19 54 9 44 9 30V12z" fill="url(#iconGrad)"/>
        <circle cx="31" cy="27" r="5" fill="#fff"/>
        <rect x="29" y="28" width="4" height="11" rx="1.5" fill="#fff"/>
      </svg>
      <p>Weekly secure direct<br>deposit with net 30<br>payment terms.</p>
    </section>

    <h2 class="requirements-title"><span class="light">REQUIREMENTS TO</span><span class="bold">BECOME A VENDOR</span></h2>

    <ul class="requirements-list">
      <li>Auto insurance</li>
      <li>Certificate of general liability insurance</li>
      <li>Workman's compensation or state issued exemption letter</li>
      <li>Drive license or state issued ID card</li>
      <li>Coverage area</li>
      <li>Any specialty licenses Any specialty licenses</li>
    </ul>

    <div class="brand"><span class="mark"></span>Brindle Property<br>Management</div>

    <p class="contact-phone">615-555-0182</p>
    <p class="contact-web">WWW.BRINDLE<b>PROPERTY</b>MANAGEMENT.COM</p>
  </main>
</body>
</html>
```